VentriLedger.Com PowerPoint

I need a PowerPoint layout for my presentations. My business is called VentriLedger.Com - my presentations teach cardiologists how to document their procedures and visits and teaches them how to bill accurately for them.

Industry/Entity Type

Business

Requirements
Must have
• the logo should be subtly there on each page - perhaps as a watermark? I'm really not creative; please help.

```html
<!DOCTYPE html>
<html lang="en">
<head>
<meta charset="utf-8">
<title>VentriLedger.Com Presentation Layout</title>
<link href="https://fonts.googleapis.com/css2?family=PT+Sans:wght@400;700&family=PT+Sans+Narrow:wght@400;700&display=swap" rel="stylesheet">
<style>
:root{
  --red:#e31b23;
  --red-dark:#8e0d14;
  --red-title:#c1202f;
  --grey-dark:#3f3f42;
  --slide-top:#ffffff;
  --slide-bottom:#dcdce6;
  --ink:#1c1c1c;
  --stage-center:#8a8a8a;
  --stage-edge:#050505;
}
*{margin:0;padding:0;box-sizing:border-box}
html,body{width:1200px;height:999px;overflow:hidden}
body{
  background:radial-gradient(ellipse 60% 55% at 50% 50%,var(--stage-center) 0%,#3a3a3a 55%,var(--stage-edge) 100%);
  font-family:"PT Sans",sans-serif;
  position:relative;
}
.slide{
  position:absolute;width:495px;height:371px;overflow:hidden;
  background:linear-gradient(180deg,var(--slide-top) 40%,var(--slide-bottom) 100%);
}
.slide-cover{left:85px;top:111px}
.slide-welcome{left:626px;top:108px}
.slide-training{left:80px;top:519px}
.slide-end{left:628px;top:515px}
.slide-art{position:absolute;inset:0;width:100%;height:100%}
.slide-title{
  position:absolute;left:0;right:0;text-align:center;
  color:var(--red-title);font-weight:700;font-size:56px;line-height:1;letter-spacing:-.5px;
}
.slide-cover .slide-title{top:196px}
.slide-end .slide-title{top:190px}
.site-url{position:absolute;font-size:11px;color:var(--ink)}
.site-url-bottom{left:8px;bottom:3px}
.site-url-top{right:26px;top:12px;color:#fff}
.brand{
  position:absolute;right:38px;bottom:8px;display:flex;align-items:center;gap:5px;
  font-size:15px;font-weight:400;color:var(--grey-dark);
}
.brand-dot{width:14px;height:14px;border-radius:50%;background:var(--red-title)}
.brand-small{font-size:11px;bottom:6px}
.brand-small .brand-dot{width:10px;height:10px}
.section-tab{
  position:absolute;left:0;top:42px;height:24px;padding:0 18px 0 28px;
  background:linear-gradient(90deg,var(--red-dark),var(--red));
  border-radius:0 14px 14px 0;color:#fff;font-weight:700;font-size:18px;line-height:24px;
}
.slide-body{
  position:absolute;left:28px;right:26px;top:71px;
  font-family:"PT Sans Narrow","PT Sans",sans-serif;font-size:9.4px;line-height:1.17;color:var(--ink);
}
.slide-body p{text-align:justify}
.subhead{font-family:"PT Sans",sans-serif;color:var(--red-title);font-weight:700;font-size:14px;margin:12px 0 0}
.lead{color:var(--red-title);font-weight:700;margin-top:11px}
.point-list{list-style:none;margin-top:9px}
.point-list li{position:relative;padding-left:19px;margin-bottom:12px;line-height:11px}
.point-list li::before{
  content:"";position:absolute;left:2px;top:2px;width:7px;height:7px;border-radius:50%;background:var(--red-title);
}
.slide-training .point-list{margin-top:13px}
</style>
</head>
<body>

<svg width="0" height="0" style="position:absolute" aria-hidden="true">
  <defs>
    <linearGradient id="bandRed" x1="0" x2="1" y1="0" y2="0">
      <stop offset="0" stop-color="#e31b23"/>
      <stop offset=".45" stop-color="#ec2128"/>
      <stop offset="1" stop-color="#7d0a10"/>
    </linearGradient>
    <linearGradient id="swooshRed" x1="0" x2="1" y1="0" y2="0">
      <stop offset="0" stop-color="#a8101a"/>
      <stop offset=".5" stop-color="#e31b23"/>
      <stop offset="1" stop-color="#f04048"/>
    </linearGradient>
    <linearGradient id="swooshGrey" x1="0" x2="1">
      <stop offset="0" stop-color="#8a8a8e"/>
      <stop offset="1" stop-color="#3a3a3e"/>
    </linearGradient>
  </defs>
</svg>

<!-- Cover slide -->
<section class="slide slide-cover">
  <svg class="slide-art" viewBox="0 0 495 371" preserveAspectRatio="none" aria-hidden="true">
    <path d="M0,0H495V70C420,80 340,150 230,150C150,150 80,95 0,100Z" fill="url(#bandRed)"/>
    <path d="M0,100C80,95 150,150 230,150C340,150 420,80 495,70" fill="none" stroke="#5a5a5e" stroke-width="5"/>
    <path d="M0,270C20,325 110,350 280,340C140,352 40,348 0,330Z" fill="url(#swooshRed)"/>
    <path d="M240,338C330,312 420,296 495,298V314C420,310 330,322 240,338Z" fill="url(#swooshGrey)"/>
  </svg>
  <h1 class="slide-title">Title Here</h1>
  <span class="site-url site-url-bottom">Ventriledger.com</span>
  <div class="brand"><span class="brand-dot"></span>VentriLedger.com</div>
</section>

<!-- Welcome slide -->
<section class="slide slide-welcome">
  <svg class="slide-art" viewBox="0 0 495 371" preserveAspectRatio="none" aria-hidden="true">
    <path d="M0,0H495V38C420,30 320,14 220,18C130,22 60,30 0,20Z" fill="url(#bandRed)"/>
    <path d="M0,20C60,30 130,22 220,18C320,14 420,30 495,38" fill="none" stroke="#5a5a5e" stroke-width="3"/>
    <path d="M0,318C30,350 120,366 260,360C140,371 40,371 0,371Z" fill="url(#swooshRed)"/>
    <path d="M240,354C330,338 420,328 495,330V340C420,338 330,344 240,354Z" fill="url(#swooshGrey)"/>
  </svg>
  <span class="site-url site-url-top">Ventriledger.com</span>
  <h2 class="section-tab">Welcome</h2>
  <div class="slide-body">
    <p>Medical conditions of the cardiology patient base require specialized care. Securing compensation for this care requires specialization too. VentriLedger.Com is uniquely qualified to facilitate full charge capture, optimal claim outcomes, effective accounts receivable, and regulatory compliance for this specialty. We consistently reduce regulatory exposure and increase collections for our clients.</p>
    <h3 class="subhead">Please consider our proficiencies:</h3>
    <ul class="point-list">
      <li>We work exclusively with cardiologists so you can rest-assured that nothing is lost in translation.</li>
      <li>We execute proprietary checks and balances to make sure that we bill each reportable service.</li>
      <li>Dan Mercer, CPC, CCC provides physician training to ensure that documentation is adequate.</li>
      <li>We conduct chart audits to screen for regulatory exposure and improvement opportunities.</li>
      <li>Our staff of over one hundred employees works exclusively from our United States based offices.</li>
      <li>We implement documentation and charge capture tools that systematically facilitate best practices.</li>
      <li>We maintain an arsenal of authoritative supporting documentation that super-charges appeal efforts.</li>
      <li>Customizable reporting empowers management to effectively run the business.</li>
    </ul>
  </div>
  <div class="brand brand-small"><span class="brand-dot"></span>VentriLedger.com</div>
</section>

<!-- Training slide -->
<section class="slide slide-training">
  <svg class="slide-art" viewBox="0 0 495 371" preserveAspectRatio="none" aria-hidden="true">
    <path d="M0,0H495V38C420,30 320,14 220,18C130,22 60,30 0,20Z" fill="url(#bandRed)"/>
    <path d="M0,20C60,30 130,22 220,18C320,14 420,30 495,38" fill="none" stroke="#5a5a5e" stroke-width="3"/>
    <path d="M0,318C30,350 120,366 260,360C140,371 40,371 0,371Z" fill="url(#swooshRed)"/>
    <path d="M240,354C330,338 420,328 495,330V340C420,338 330,344 240,354Z" fill="url(#swooshGrey)"/>
  </svg>
  <span class="site-url site-url-top">Ventriledger.com</span>
  <h2 class="section-tab">Training Programs</h2>
  <div class="slide-body">
    <p>Dan Mercer, CPC, CCC has trained cardiologists and billers to secure accurate reimbursement and achieve regulatory compliance for 21 years. He has worked as an independent consultant and as an employee of two large cardiology groups (Heartline Group in Indianapolis, IN and Larkfield Cardiac Partners in Charlotte, NC). He directed the development of the National Guild of Clinical Coders specialty coding certification titled “Certified Cardiac Coding Specialist” and has facilitated thousands of training programs for medical device companies Valvera Devices, Pulsewright Scientific, and Northgate Medical.</p>
    <p class="lead">Dan provides training programs for physicians and billing professionals that help them achieve coding and documentation proficiency in each of the cardiology specialty areas:</p>
    <ul class="point-list">
      <li>Heart catheterization &amp; coronary intervention</li>
      <li>Pacemaker &amp; defibrillator surgery and follow-up</li>
      <li>Peripheral vascular angiography &amp; intervention</li>
      <li>Electrophysiology studies &amp; ablation procedures</li>
      <li>Evaluation and management services</li>
    </ul>
  </div>
  <div class="brand brand-small"><span class="brand-dot"></span>VentriLedger.com</div>
</section>

<!-- Closing slide -->
<section class="slide slide-end">
  <svg class="slide-art" viewBox="0 0 495 371" preserveAspectRatio="none" aria-hidden="true">
    <path d="M0,0H495V85C420,100 340,150 230,150C150,150 80,105 0,110Z" fill="url(#bandRed)"/>
    <path d="M0,110C80,105 150,150 230,150C340,150 420,100 495,85" fill="none" stroke="#5a5a5e" stroke-width="5"/>
    <path d="M0,270C20,325 110,350 280,340C140,352 40,348 0,330Z" fill="url(#swooshRed)"/>
    <path d="M240,338C330,312 420,296 495,298V314C420,310 330,322 240,338Z" fill="url(#swooshGrey)"/>
  </svg>
  <h1 class="slide-title">The End</h1>
  <span class="site-url site-url-bottom">Ventriledger.com</span>
  <div class="brand"><span class="brand-dot"></span>VentriLedger.com</div>
</section>

</body>
</html>
```